SkyVane Weather Newsletter Design

Attached is a copy of a weekly newsletter that contains commentary and maps used to discuss all relevant information about weather forecasts. I need to create a newsletter (template) where content can be systematically input into a unique SkyVane format. The object is to deliver a unique design that captures the essence of the firm, the brand, and can be easily used by the team developing the maps and narrative. All logo and related background information may be obtained on the Skyvane website.
Updates

I am just checking to see if there is any interest anywhere in this type of project. This project requires a combination of layout skills and border design work. Any feedback?Dale Added Friday, May 6, 2016

Target Market(s)

Institutional users of weather data, airports, military, governmental agencies, oil companies, news broadcasters, etc.

Requirements
Must have
• Unique design and format. Flexibility to place a number of maps in and around narrative used in the weekly newsletter.
Nice to have
• We have no preference on font. If additional photos of maps are required, please inquire.
Should not have
• Have one solid background color that will use a lot of toner if needed to print out. It can often clash with the multi color nature of the maps.

```html
<!DOCTYPE html>
<html lang="en">
<head>
<meta charset="utf-8">
<title>SkyVane – Daily Weather Newsletter</title>
<link rel="stylesheet" href="https://fonts.googleapis.com/css2?family=Jost:wght@300;400;600;700&display=swap">
<style>
  :root {
    --page-bg: #e9e9e9;
    --page-dot: #c9c9c9;
    --sheet: #ffffff;
    --divider: #e2e2e2;
    --brand: #1b72b8;
    --brand-dark: #1a00a3;
    --ink: #111111;
    --sky-top: #2f7fd1;
    --sky-mid: #8dbbe6;
    --cloud: #eef2f7;
    --map-land: #6d6f63;
    --map-edge: #8a8f86;
  }
  * { box-sizing: border-box; margin: 0; padding: 0; }
  html, body {
    width: 1029px;
    height: 1200px;
    overflow: hidden;
  }
  body {
    position: relative;
    background-color: var(--page-bg);
    background-image: radial-gradient(var(--page-dot) 1px, transparent 1.2px);
    background-size: 22px 22px;
    font-family: "Jost", "Futura", sans-serif;
    color: var(--ink);
  }
  .newsletter {
    position: absolute;
    left: 204px;
    top: 0;
    width: 620px;
  }
  .masthead {
    height: 114px;
    background: var(--sheet);
    display: flex;
    align-items: center;
    justify-content: center;
  }
  .brand {
    display: flex;
    align-items: center;
    gap: 12px;
  }
  .brand-mark {
    width: 24px;
    height: 24px;
    background: var(--brand);
  }
  .brand-name {
    font-size: 46px;
    font-weight: 600;
    color: var(--brand);
    line-height: 1;
  }
  .hero {
    height: 228px;
    background:
      radial-gradient(ellipse 42% 55% at 70% 70%, var(--cloud) 0%, rgba(238,242,247,0.85) 45%, transparent 75%),
      radial-gradient(ellipse 30% 55% at 18% 40%, rgba(238,242,247,0.9) 0%, transparent 70%),
      linear-gradient(180deg, var(--sky-top) 0%, var(--sky-mid) 100%);
  }
  .issue {
    height: 122px;
    background: var(--sheet);
    text-align: center;
    padding-top: 24px;
    border-bottom: 8px solid var(--divider);
  }
  .issue-title {
    font-size: 21px;
    font-weight: 600;
    line-height: 1.25;
  }
  .issue-edition, .issue-date {
    font-size: 18px;
    font-weight: 300;
    line-height: 1.35;
  }
  .commentary {
    height: 263px;
    background: var(--sheet);
    padding: 18px 18px 0 18px;
  }
  .greeting {
    font-size: 20px;
    font-weight: 600;
    margin-bottom: 20px;
  }
  .commentary p {
    font-size: 18.5px;
    font-weight: 300;
    line-height: 1.35;
    hyphens: auto;
    -webkit-hyphens: auto;
  }
  .map {
    margin-top: 15px;
    height: 450px;
    background:
      radial-gradient(ellipse 18% 20% at 80% 85%, rgba(90,170,70,0.7), transparent 70%),
      radial-gradient(ellipse 12% 10% at 40% 75%, rgba(210,140,220,0.6), transparent 70%),
      radial-gradient(ellipse 15% 12% at 88% 55%, rgba(210,140,220,0.6), transparent 70%),
      linear-gradient(160deg, var(--map-edge) 0%, var(--map-land) 55%, #5e6157 100%);
  }
  .share-bar {
    position: absolute;
    left: 164px;
    top: 115px;
    display: flex;
    flex-direction: column;
    gap: 11px;
    list-style: none;
  }
  .share-bar li {
    width: 40px;
    height: 36px;
    background: var(--brand-dark);
    border-radius: 4px 0 0 4px;
    display: flex;
    align-items: center;
    justify-content: center;
  }
</style>
</head>
<body>
  <ul class="share-bar">
    <li aria-label="Home">
      <svg width="16" height="14" viewBox="0 0 16 14"><path d="M8 1 L15 7 H13 V13 H10 V9 H6 V13 H3 V7 H1 Z" fill="#fff"/></svg>
    </li>
    <li aria-label="Print">
      <svg width="16" height="14" viewBox="0 0 16 14"><rect x="4" y="1" width="8" height="4" fill="none" stroke="#fff" stroke-width="1.4"/><rect x="1" y="5" width="14" height="6" fill="#fff"/><rect x="4" y="9" width="8" height="4" fill="#fff" stroke="#1a00a3" stroke-width="1"/></svg>
    </li>
    <li aria-label="Share on social network"></li>
    <li aria-label="Share on social network"></li>
    <li aria-label="Watch video channel"></li>
  </ul>

  <main class="newsletter">
    <header class="masthead">
      <div class="brand">
        <span class="brand-mark"></span>
        <span class="brand-name">SkyVane</span>
      </div>
    </header>

    <div class="hero" role="img" aria-label="Photo of white cumulus clouds against a blue sky"></div>

    <section class="issue">
      <h1 class="issue-title">Daily Weather Newsletter</h1>
      <p class="issue-edition">Southeast Edition</p>
      <p class="issue-date">May 3, 2016</p>
    </section>

    <article class="commentary">
      <h2 class="greeting">Good Morning from Houston,</h2>
      <p>The Southeast experienced more severe weather yesterday, but this time, Kentucky, Tennessee, Virginia and the Carolinas were the target.&nbsp; No tornadoes were reported, but there was plenty of hail; some as large as 2 inches in diameter.&nbsp; There were also lots of reports of wind damage, with a reported maximum over 70 miles per hour.<br>
      The storms will remain along the East Coast and Gulf Coast today, going from Virginia to Alabama with the strongest threat over the Carolinas.</p>
    </article>

    <div class="map" role="img" aria-label="Surface analysis map of North America with radar and satellite overlay, fronts and pressure systems"></div>
  </main>
</body>
</html>
```